Brivora Collective Business Card Design

We need a business card design for Brivora Collective. We are a healthcare recruiting, wellness and education company. We partner with medical facilities to find quality candidates. We also offer free wellness courses.
The final design should communicate an emphasis on recruiting and wellness
The main purpose of the business card is to utilized it for networking events, give to hospitals, executives, VCs surgery centers and clinics. I want it to be sleek, clean, use of our brand colors and professional.

```html
<!DOCTYPE html>
<html lang="en">
<head>
<meta charset="utf-8">
<title>Brivora Collective – Business Card</title>
<link rel="stylesheet" href="https://fonts.googleapis.com/css2?family=Open+Sans:wght@400;700&display=swap">
<style>
  :root {
    --backdrop: #3c3c3c;
    --card: #161616;
    --card-edge: #0c0c0c;
    --teal: #0f5f59;
    --white: #f2f2f2;
    --emboss: #070707;
    --emboss-mark: #8c8c8c;
  }
  * { margin: 0; padding: 0; box-sizing: border-box; }
  html, body {
    width: 1200px; height: 780px; overflow: hidden;
    background: var(--backdrop);
    font-family: "Open Sans", Arial, sans-serif;
  }
  .canvas {
    width: 1200px; height: 780px;
    display: flex; align-items: center; justify-content: center; gap: 40px;
  }
  .card {
    position: relative;
    width: 520px; height: 300px;
    background: var(--card);
    border-radius: 22px;
    box-shadow: 0 6px 0 var(--card-edge), 0 20px 40px rgba(0,0,0,.45);
    overflow: hidden;
  }
  /* Front: contact side */
  .card-front { display: flex; align-items: center; }
  .brand-block {
    width: 250px; padding-left: 34px;
  }
  .brand-name {
    color: var(--teal);
    font-weight: 400;
    font-size: 30px;
    line-height: 1.05;
    letter-spacing: -0.5px;
  }
  .divider {
    width: 1px; height: 170px;
    background: var(--teal);
  }
  .contact-block {
    padding-left: 24px;
    color: var(--white);
    font-size: 13px;
    line-height: 1.55;
  }
  .person-name {
    color: var(--teal);
    font-weight: 700;
    font-size: 19px;
    letter-spacing: 0.5px;
    line-height: 1.2;
  }
  .person-title { margin-bottom: 6px; }
  .contact-line { display: flex; align-items: center; gap: 7px; }
  .contact-line svg { width: 12px; height: 12px; flex: none; }
  .address { margin-top: 6px; line-height: 1.45; }

  /* Back: brand side */
  .card-back { display: flex; align-items: center; justify-content: center; gap: 16px; }
  .back-mark {
    width: 46px; height: 46px;
    background: var(--emboss-mark);
    border-radius: 8px;
  }
  .back-name {
    color: var(--emboss);
    font-weight: 400;
    font-size: 44px;
    line-height: 1.05;
    letter-spacing: -1px;
  }
</style>
</head>
<body>
<main class="canvas">
  <section class="card card-front" aria-label="Business card front">
    <div class="brand-block">
      <p class="brand-name">Brivora<br>Collective</p>
    </div>
    <div class="divider"></div>
    <div class="contact-block">
      <p class="person-name">DANIEL HAYES</p>
      <p class="person-title">Managing Director</p>
      <p class="contact-line">
        <svg viewBox="0 0 12 12" aria-hidden="true"><circle cx="6" cy="6" r="6" fill="var(--teal)"/><path d="M3.6 3.2l1.2-.4.8 1.6-.7.6c.4.8 1 1.4 1.8 1.8l.6-.7 1.6.8-.4 1.2C6.4 8.5 3.5 5.6 3.6 3.2z" fill="var(--white)"/></svg>
        123 456 789
      </p>
      <p class="contact-line">
        <svg viewBox="0 0 12 12" aria-hidden="true"><circle cx="6" cy="6" r="6" fill="var(--teal)"/><rect x="3" y="4" width="6" height="4.2" fill="none" stroke="var(--white)" stroke-width=".9"/><path d="M3 4l3 2.4L9 4" fill="none" stroke="var(--white)" stroke-width=".9"/></svg>
        info@yourgmail.com
      </p>
      <p class="contact-line">
        <svg viewBox="0 0 12 12" aria-hidden="true"><circle cx="6" cy="6" r="6" fill="var(--teal)"/><circle cx="6" cy="6" r="3.2" fill="none" stroke="var(--white)" stroke-width=".8"/><path d="M2.8 6h6.4M6 2.8c-1.6 1.8-1.6 4.6 0 6.4M6 2.8c1.6 1.8 1.6 4.6 0 6.4" fill="none" stroke="var(--white)" stroke-width=".7"/></svg>
        www.yourwebsite.com
      </p>
      <p class="address">Your address, City<br>State, Zip 1234</p>
    </div>
  </section>

  <section class="card card-back" aria-label="Business card back">
    <div class="back-mark"></div>
    <p class="back-name">Brivora<br>Collective</p>
  </section>
</main>
</body>
</html>
```